Business Card Design Project

We need a business card designed for a new Luxury Custom Homebuilding company based in Arizona. We previous were called "Belcrest Estates" but want to start using "Belcrest Custom Homes" We want the message to communicate high end, luxury and cutting-edge. We like the blue, white and black color scheme.
Belcrest Custom Homes
Marcus T. Halloway
Chief Executive Officer
Office: 480-555-0142
Mobile: 480-555-0178
email: marc@belcrestcustom-example.com
web adress: www.BelcrestCustom-example.com
Updates
We have made a change to our website address and email address based on recieving feedback from a nmber of individuals. The feedback was web address and email address was to long. Therefore we have made a change. The new web adress and email adress are the following.
www.BelcrestCustom-example.com
marc@belcrestcustom-example.com
Also I decided against using in yellow. I like the colors blue,black, white and maybe gray.
Target Market(s)
Our target market is the wealthy individuals looking for a luxury high-end custom home.
Industry/Entity Type
Business
Look and feel

```html
<!DOCTYPE html>
<html lang="en">
<head>
<meta charset="utf-8">
<title>Belcrest Custom Homes – Business Card</title>
<link rel="stylesheet" href="https://fonts.googleapis.com/css2?family=Source+Sans+3:wght@400;600;700&display=swap">
<style>
  :root {
    --page: #ffffff;
    --blue-deep: #1f6aa8;
    --blue-mid: #3f86c4;
    --blue-light: #6aa3d6;
    --ink: #333333;
    --white: #ffffff;
    --shadow: rgba(0, 0, 0, 0.35);
  }
  * { box-sizing: border-box; margin: 0; padding: 0; }
  html, body {
    width: 1200px; height: 1000px; overflow: hidden;
    background: var(--page);
    font-family: "Source Sans 3", "Myriad Pro", sans-serif;
  }
  .canvas { position: relative; width: 1200px; height: 1000px; }

  .card {
    position: absolute; left: 284px; width: 658px; height: 375px;
    overflow: hidden;
    box-shadow: 2px 4px 6px var(--shadow);
  }
  .card--front {
    top: 94px;
    background: radial-gradient(ellipse at 60% 35%, var(--blue-light) 0%, var(--blue-mid) 45%, var(--blue-deep) 100%);
  }
  .card--back { top: 533px; background: var(--white); }

  .card__art { position: absolute; inset: 0; width: 100%; height: 100%; }

  .wordmark {
    position: absolute; left: 0; right: 0; text-align: center;
    font-weight: 700; line-height: 0.9; letter-spacing: -1px;
  }
  .wordmark__name { display: block; font-size: 82px; }
  .wordmark__sub { display: block; font-size: 30px; letter-spacing: 1px; text-transform: uppercase; margin-top: 6px; }
  .card--front .wordmark { top: 138px; color: var(--white); }
  .card--back .wordmark { top: 60px; color: var(--ink); }

  .front-url {
    position: absolute; left: 0; right: 0; top: 333px;
    text-align: center; color: var(--white);
    font-size: 15px; letter-spacing: 0.6px;
  }

  .contact {
    position: absolute; left: 56px; top: 255px;
    list-style: none; color: var(--white); font-size: 16px;
  }
  .contact li { display: flex; align-items: center; height: 22px; }
  .contact svg { width: 16px; height: 16px; margin-right: 9px; fill: var(--white); }

  .person {
    position: absolute; right: 42px; top: 273px;
    text-align: right; color: var(--white);
  }
  .person__name { font-size: 21px; font-weight: 700; line-height: 1.1; }
  .person__title { font-size: 16px; margin-top: 4px; }
</style>
</head>
<body>
<main class="canvas">

  <section class="card card--front">
    <svg class="card__art" viewBox="0 0 658 375" preserveAspectRatio="none" aria-hidden="true">
      <path d="M0,70 Q330,40 658,0 L658,20 Q330,70 0,80 Z" fill="#ffffff" opacity="0.08"/>
      <path d="M0,190 Q360,140 658,80 L658,200 Q360,220 0,230 Z" fill="#ffffff" opacity="0.1"/>
      <path d="M0,250 Q330,270 658,230 L658,290 Q330,320 0,300 Z" fill="#ffffff" opacity="0.07"/>
    </svg>
    <h1 class="wordmark">
      <span class="wordmark__name">Belcrest</span>
      <span class="wordmark__sub">Custom Homes</span>
    </h1>
    <p class="front-url">www.BelcrestCustom-example.com</p>
  </section>

  <section class="card card--back">
    <svg class="card__art" viewBox="0 0 658 375" preserveAspectRatio="none" aria-hidden="true">
      <defs>
        <radialGradient id="backBlue" cx="0.5" cy="0.75" r="0.7">
          <stop offset="0" stop-color="#5b98d2"/>
          <stop offset="1" stop-color="#1f6aa8"/>
        </radialGradient>
      </defs>
      <path d="M0,200 Q300,262 658,162 L658,375 L0,375 Z" fill="url(#backBlue)"/>
      <path d="M180,238 Q430,238 658,170 L658,178 Q430,248 180,238 Z" fill="#ffffff"/>
      <path d="M380,232 Q560,220 658,142 L658,156 Q560,232 380,232 Z" fill="#1f6aa8"/>
      <path d="M0,162 Q200,212 425,214 Q200,228 0,192 Z" fill="#333333"/>
    </svg>
    <h2 class="wordmark">
      <span class="wordmark__name">Belcrest</span>
      <span class="wordmark__sub">Custom Homes</span>
    </h2>
    <ul class="contact">
      <li><svg viewBox="0 0 16 16" aria-hidden="true"><path d="M1,6 Q8,0 15,6 L13,8 L11,6 L11,5 Q8,4 5,5 L5,6 L3,8 Z M4,9 L12,9 L14,14 L2,14 Z"/></svg>480-555-0142</li>
      <li><svg viewBox="0 0 16 16" aria-hidden="true"><path d="M4,1 H12 V15 H4 Z M5.5,2.5 V12 H10.5 V2.5 Z"/></svg>480-555-0178</li>
      <li><svg viewBox="0 0 16 16" aria-hidden="true"><path d="M1,3 H15 V13 H1 Z M2,4.5 V12 H14 V4.5 L8,9 Z M2.5,4 L8,8 L13.5,4 Z" fill-rule="evenodd"/></svg>marc@belcrestcustom-example.com</li>
      <li><svg viewBox="0 0 16 16" aria-hidden="true"><path d="M8,1 A7,7 0 1 0 8.01,1 Z M8,2.4 A5.6,5.6 0 1 1 7.99,2.4 Z M7.3,2 H8.7 V14 H7.3 Z M2,7.3 H14 V8.7 H2 Z" fill-rule="evenodd"/></svg>www.BelcrestCustom-example.com</li>
    </ul>
    <div class="person">
      <p class="person__name">Marcus T. Halloway</p>
      <p class="person__title">Chief Executive Officer</p>
    </div>
  </section>

</main>
</body>
</html>
```